Fatigued and Overloaded by COVID Messages? We need original illustrations to show that.

Everywhere you look there are messages about COVID. That is leading many people to feel fatigued and overloaded by the messages.

We surveyed U.S. adults March 20th - 24th, 2020 and measured message fatigue, information overload, perceived repetition, and perceived exaggeration. Here is how participants responded:

When it comes to coronavirus . . .
55% feel exhausted by all the messages.
54% feel overloaded by the amount of information.
51% feel that the messages are repetitive.
47% feel like messages exaggerate how bad it is.

In other words, almost half of U.S. adults show signs of message fatigue, information overload, perceived message repetition, and perceived message exaggeration.

We will continue to survey 400 adults every week for the next 16 weeks. Each time we will measure message fatigue, information overload, perceived repetition, and perceived exaggeration. We expect that it will increase over time.

What are we looking for? We need innovative and original illustrations that attempt to communicate these findings. The illustrations would visualize message fatigue, information overload, perceived message repetition, and perceived message exaggeration.

What sort of visual are we looking for? Our preference is for an original illustration (or set of illustrations). Our preference is for creative and powerful illustrations, but we are also open to the creative and well-executed infographics.

We need these images fast . We will award monetary prizes to the 3 best designs. If we like more than that, then we might purchase more (e.g., in past contests, we have purchased as many as 30 designs).

What we will need:
(1) The illustrations must be original and we will need the photoshop and/or illustrator files for all artwork. (By original, we mean that the illustrations are 100% created by you. Our organization requires that we utilize only original illustrated work. We have had issues with free imagery being pirated and reposted as free. We sidestep that issue by just having everything created.)

(2) The illustration should say, somewhere: "Based on a survey of 400 U.S. adults conducted March 20 - 24th, 2020."

(3) We will have almost 4 months worth of data by the time this is done. In other words, the illustrations might be able to help us present that weekly data.

(4) We have conducted other Artvendo projects. It might be helpful to examine designs we liked in the past. For example, here is another COVID project we just finished:

https://jobs.artvendo-example.com/job/5162048

Target Market(s)

U.S. adults

Requirements
Must have
• Original illustrations. Mobile friendly design. People will view this on their smartphones.
Nice to have
• A design that we can use to communicate the data across time.

```html
<!DOCTYPE html>
<html lang="en">
<head>
<meta charset="utf-8">
<title>Fatigued and Overloaded by COVID-19 Messages?</title>
<link rel="stylesheet" href="https://fonts.googleapis.com/css2?family=Comfortaa:wght@500;600;700&display=swap">
<style>
  :root {
    --maroon: #7f0000;
    --navy: #003e77;
    --ink-blue: #0e3c6e;
    --white: #ffffff;
    --bg-light: #f1f1f3;
    --bg-edge: #d6d6d8;
    --gap: #f4f4f6;
  }
  * { margin: 0; padding: 0; box-sizing: border-box; }
  html, body { width: 1200px; height: 1200px; overflow: hidden; }
  body {
    font-family: "Comfortaa", sans-serif;
    background: var(--bg-edge);
  }
  .canvas {
    position: relative;
    width: 1200px;
    height: 1200px;
    overflow: hidden;
    background: radial-gradient(circle at 50% 50%, var(--bg-light) 0%, #e6e6e8 55%, var(--bg-edge) 100%);
  }
  .title-shadow {
    position: absolute;
    left: 180px; top: 47px;
    width: 858px; height: 180px;
    background: var(--navy);
    border-radius: 62px;
  }
  .title-box {
    position: absolute;
    left: 160px; top: 24px;
    width: 863px; height: 186px;
    background: var(--maroon);
    border-radius: 62px;
    display: flex;
    flex-direction: column;
    justify-content: center;
    align-items: center;
  }
  .title {
    color: var(--white);
    font-weight: 700;
    font-size: 60px;
    line-height: 68px;
    text-align: center;
    letter-spacing: 1.5px;
  }
  .lead {
    position: absolute;
    left: 0; top: 237px;
    width: 1200px;
    text-align: center;
    color: var(--maroon);
    font-weight: 600;
    font-size: 42px;
    letter-spacing: 3px;
  }
  .connectors {
    position: absolute;
    left: 0; top: 0;
    width: 1200px; height: 1200px;
  }
  .pie {
    position: absolute;
    width: 250px; height: 250px;
  }
  .pie svg { position: absolute; left: 0; top: 0; }
  .pie-value {
    position: absolute;
    left: 0; top: 42px;
    width: 250px;
    text-align: center;
    color: var(--white);
    font-weight: 700;
    font-size: 44px;
  }
  .pie-label {
    position: absolute;
    width: 400px;
    text-align: center;
    color: var(--ink-blue);
    font-weight: 600;
    font-size: 25px;
    line-height: 30px;
    letter-spacing: 1.5px;
  }
  .pie--exhausted { left: 88px; top: 317px; }
  .pie--overloaded { left: 862px; top: 317px; }
  .pie--repetitive { left: 88px; top: 779px; }
  .pie--exaggerated { left: 862px; top: 779px; }
  .label--exhausted { left: 13px; top: 575px; }
  .label--overloaded { left: 787px; top: 577px; width: 400px; }
  .label--repetitive { left: 13px; top: 1039px; }
  .label--exaggerated { left: 787px; top: 1039px; }
  .hero-illustration {
    position: absolute;
    left: 413px; top: 435px;
    width: 374px; height: 525px;
    border-radius: 40px;
    background: radial-gradient(ellipse at 50% 70%, #3b5f94 0%, #6a7fa8 35%, #c9cbd6 75%, rgba(230,230,232,0) 100%);
  }
  .source-note {
    position: absolute;
    left: 0; top: 1154px;
    width: 1200px;
    text-align: center;
    color: var(--maroon);
    font-weight: 700;
    font-size: 20px;
    letter-spacing: 0.3px;
  }
</style>
</head>
<body>
<main class="canvas">
  <div class="title-shadow"></div>
  <header class="title-box">
    <h1 class="title">Fatigued and Overloaded<br>by COVID-19 Messages?</h1>
  </header>

  <p class="lead">When it comes to coronavirus . . .</p>

  <svg class="connectors" width="1200" height="1200" viewBox="0 0 1200 1200" aria-hidden="true">
    <g fill="none" stroke="#003e77" stroke-width="4.5">
      <polyline points="634,417 634,376 836,376"/>
      <polyline points="211,676 211,723 460,723"/>
      <polyline points="755,713 987,713 987,735"/>
      <polyline points="620,987 620,1074 429,1074"/>
    </g>
    <g fill="#003e77">
      <rect x="824" y="363" width="25" height="25"/>
      <rect x="199" y="651" width="25" height="25"/>
      <rect x="975" y="733" width="25" height="25"/>
      <rect x="405" y="1062" width="25" height="25"/>
    </g>
  </svg>

  <div class="hero-illustration" role="img" aria-label="Illustration of a stressed office worker sitting cross-legged, hand on forehead, under a swirl of flying documents and angry virus particles"></div>

  <!-- 55% -->
  <div class="pie pie--exhausted">
    <svg width="250" height="250" viewBox="-125 -125 250 250" aria-hidden="true">
      <path d="M122 0 A122 122 0 1 0 -118 31 L0 0 Z" fill="#003e77" stroke="#f4f4f6" stroke-width="5" stroke-linejoin="round"/>
      <path d="M-118 31 A122 122 0 0 0 122 0 L0 0 Z" fill="#7f0000" stroke="#f4f4f6" stroke-width="5" stroke-linejoin="round"/>
    </svg>
    <div class="pie-value">55%</div>
  </div>
  <p class="pie-label label--exhausted">Feel exhausted by<br>all the messages.</p>

  <!-- 54% -->
  <div class="pie pie--overloaded">
    <svg width="250" height="250" viewBox="-125 -125 250 250" aria-hidden="true">
      <path d="M122 0 A122 122 0 1 0 -121 15 L0 0 Z" fill="#003e77" stroke="#f4f4f6" stroke-width="5" stroke-linejoin="round"/>
      <path d="M-121 15 A122 122 0 0 0 122 0 L0 0 Z" fill="#7f0000" stroke="#f4f4f6" stroke-width="5" stroke-linejoin="round"/>
    </svg>
    <div class="pie-value">54%</div>
  </div>
  <p class="pie-label label--overloaded">Feel overloaded by<br>the amount of information.</p>

  <!-- 51% -->
  <div class="pie pie--repetitive">
    <svg width="250" height="250" viewBox="-125 -125 250 250" aria-hidden="true">
      <path d="M122 0 A122 122 0 1 0 -122 8 L0 0 Z" fill="#003e77" stroke="#f4f4f6" stroke-width="5" stroke-linejoin="round"/>
      <path d="M-122 8 A122 122 0 0 0 122 0 L0 0 Z" fill="#7f0000" stroke="#f4f4f6" stroke-width="5" stroke-linejoin="round"/>
    </svg>
    <div class="pie-value">51%</div>
  </div>
  <p class="pie-label label--repetitive">Feel that the messages<br>are repetitive.</p>

  <!-- 47% -->
  <div class="pie pie--exaggerated">
    <svg width="250" height="250" viewBox="-125 -125 250 250" aria-hidden="true">
      <path d="M122 0 A122 122 0 0 0 -121 -16 L0 0 Z" fill="#003e77" stroke="#f4f4f6" stroke-width="5" stroke-linejoin="round"/>
      <path d="M-121 -16 A122 122 0 1 0 122 0 L0 0 Z" fill="#7f0000" stroke="#f4f4f6" stroke-width="5" stroke-linejoin="round"/>
    </svg>
    <div class="pie-value">47%</div>
  </div>
  <p class="pie-label label--exaggerated">Feel like messages<br>exaggerate how bad it is.</p>

  <p class="source-note">"Based on a survey of 400 U.S. adults conducted March 20 - 24th, 2020."</p>
</main>
</body>
</html>
```